Postcard to alert practices of a new dermatology practice opening

We are opening a dermatology practice and need a front and back postcard that we can drop off to practices and friends to alert them of our opening, as well as what we offer:
Would like the colors to be bright nice blue, white, and dark gray.
Also - i am attaching the logo we already have (would like the card to be more of a blue color - not the logo color ), an example of a flyer, and a picture of me to add to the postcard mailer

Front of card:
Verandell Dermatology and Skin Surgery Associates

Now scheduling appointments. Call us (555)-014-7280!

Specializing in
- Mohs surgery by a Fellowship-Trained Mohs Surgeon
- Comprehensive dermatologic care including medical, cosmetic and surgical dermatology
- Individualized care for every patient using state of the art techniques

Corinne T. Valdemar, MD, FAAD
Board-Certified Dermatologist and Fellowship-Trained Mohs Surgeon

Dr. Valdemar graduated from the Brackenfield State University Medical School, Sigma Rho Delta, and completed her dermatology residency and Mohs fellowship at Whitcombe University in Atlanta GA. She provides complete dermatologic care for the whole family with a specialization in Mohs surgery.

4471 Quillan Avenue, Suite 100
Charlotte, NC 28999
Tel. (555)-014-7280
Fax. (555) 014-5193
www.VerandellDermatology.example

Please add logos for NGSM, CUCS, FBMS (can find on my webpage the logos)

Back of card:
About Dr. Valdemar
Dr. Corinne Tolliver Valdemar is a Board-Certified Dermatologist and Fellowship-Trained Mohs Surgeon from Whitcombe University. She graduated Tau Zeta Mu and with highest distinction from the Brackenfield State University. She then received her M.D. and Master’s in Public Health from the Brackenfield State University School of Medicine. Graduating at the top of her class, Dr. Valdemar was inducted into the prestigious Sigma Rho Delta honor society, which is the highest academic honor in medical school.

Dr. Valdemar completed her internship at Fernhollow hospital in Salt Lake City, Utah. She completed her dermatology residency training at Whitcombe University School of Medicine, serving as the Chief Resident during her final year. During her time as a resident, she received the CUCS resident scholarship award and worked with leading experts in both cutaneous and transplant oncology.
After her residency she went on to receive highly competitive sub-specialty training and completed her fellowship training in Mohs Micrographic Surgery, Cutaneous Oncology, and Reconstructive Surgery at Whitcombe University Department of Dermatology. This Procedural Dermatology fellowship is certified both by the Federated Board of Margin Surgery (FBMS) and the Physicians’ League Oversight Board for Residency Training (PLOBRT). During her training Dr. Valdemar performed thousands of dermatologic surgeries.

She has authored numerous scientific articles and textbook chapters, spoken at national meetings and served on numerous committees. Dr. Valdemar is Board Certified in Dermatology and is a Fellow of the National Guild of Skin Medicine and Federated Board of Margin Surgery. She is a member of the National Guild of Skin Medicine, Continental Union of Cutaneous Surgery, Lantern Circle Skin Society, Global Graft Recipient Melanoma Network, Sigma Rho Delta National Honor Society, and Piedmont Skin Physicians Alliance.

Prior to moving back to North Carolina, she practiced with Riverbend Skin Partners in Cincinnati performing Mohs surgery, skin surgeries, general dermatology, and cosmetics.

also put map of location and contact information for practice again.

Font styles to use
Serif

Colors
0455a3
ffffff
919191

Requirements
Must have
• on the back of the card - put a map of the practice as well as my about dr. valdemar
• front of the card - multiple pictures (can take from my website) and information about what I specialize in, location, phone number, website
Nice to have
• would like it simple and clean just like the example I provided. Mostly white background with font in a nice blue color and a dark grey. with simple clean lines
Should not have
• DO NOT put my face on the front of the card - should only be on back of card
• DO NOT put lines on the back of the card - i will not be mailing these
• DO NOT add fancy bullets

```html
<!DOCTYPE html>
<html lang="en">
<head>
<meta charset="utf-8">
<title>Verandell Dermatology Postcard</title>
<link rel="stylesheet" href="https://fonts.googleapis.com/css2?family=Questrial&family=Open+Sans:wght@400;600&display=swap">
<style>
:root{
  --blue:#0a6fc2;
  --blue-bright:#1a86d6;
  --blue-deep:#0455a3;
  --ink:#3b3d42;
  --grey:#919191;
  --paper:#ffffff;
  --stage:#d9d9d9;
}
*{margin:0;padding:0;box-sizing:border-box}
html,body{width:930px;height:1200px;overflow:hidden;background:var(--stage)}
h1,h2{font-weight:400}
.canvas{position:relative;width:930px;height:1200px}
.card{position:absolute;left:35px;width:860px;height:558px;overflow:hidden;
  background:linear-gradient(180deg,#ffffff 0%,#f7f8fa 60%,#eef0f3 100%);
  box-shadow:0 2px 8px rgba(0,0,0,.25);font-family:"Open Sans",sans-serif;color:var(--ink)}
.card--front{top:28px}
.card--back{top:614px}
.shapes{position:absolute;inset:0;width:860px;height:558px}
.tab-label{position:absolute;right:16px;top:12px;color:#fff;font-family:"Open Sans",sans-serif;
  font-size:13px;line-height:17px;text-align:right;font-weight:600}
.tab-label span{font-weight:400}
.photo{position:absolute}
.photo--circle{border-radius:50%;border:5px solid #fff;box-shadow:0 2px 6px rgba(0,0,0,.3)}
/* front */
.headline{position:absolute;left:32px;top:24px;font-family:"Questrial",sans-serif;color:var(--blue);font-weight:400}
.headline__lead{font-size:38px;line-height:46px}
.headline__sub{font-size:27px;line-height:34px}
.family-photo{left:430px;top:60px;width:430px;height:380px;
  background:radial-gradient(ellipse at 55% 45%,#e8c3a6 0%,#d7a688 30%,#c9ccd2 62%,rgba(240,242,245,0) 80%)}
.specialties{position:absolute;left:0;top:176px;width:345px}
.specialties__title{background:var(--ink);color:#fff;font-family:"Questrial",sans-serif;font-size:20px;font-weight:400;
  height:36px;line-height:36px;padding-left:32px;border-radius:0 8px 0 0}
.specialties__list{background:linear-gradient(180deg,var(--blue-bright),var(--blue-deep));list-style:none;
  padding:10px 14px 9px 32px;border-radius:0 0 8px 0}
.specialties__list li{position:relative;color:#fff;font-size:13px;line-height:17px;padding-left:22px;margin-bottom:10px}
.specialties__list li:last-child{margin-bottom:0}
.specialties__list svg{position:absolute;left:0;top:3px;width:12px;height:12px}
.brand{position:absolute;display:flex;align-items:center;gap:10px}
.brand__mark{width:44px;height:44px;border-radius:50%;border:2px solid var(--blue-bright);flex:none}
.brand__name{font-family:"Questrial",sans-serif;color:var(--blue-bright);font-size:20px;line-height:21px}
.brand--front{left:32px;top:344px}
.contact{position:absolute;color:#fff;font-size:15px;line-height:20px;display:flex;align-items:center;gap:10px;white-space:nowrap}
.contact svg{width:14px;height:14px;flex:none}
/* back */
.doctor-name{position:absolute;left:18px;top:16px;color:#fff;font-family:"Questrial",sans-serif;font-size:24px;line-height:28px}
.doctor-title{position:absolute;left:18px;top:46px;color:#e6f1fb;font-family:"Questrial",sans-serif;font-size:14px}
.portrait{left:18px;top:98px;width:136px;height:136px;background:linear-gradient(160deg,#6b5144,#b98a70 55%,#2f3a4c)}
.intro{position:absolute;left:190px;top:104px;width:650px;font-size:14.5px;line-height:19px;color:var(--ink)}
.about-pill{position:absolute;left:180px;top:196px;height:28px;padding:0 22px;border-radius:14px;
  background:var(--blue-bright);color:#fff;font-family:"Questrial",sans-serif;font-size:16px;line-height:28px}
.brand--back{right:22px;top:190px}
.brand--back .brand__mark{width:40px;height:40px}
.brand--back .brand__name{font-size:19px;line-height:19px}
.bio{position:absolute;top:254px;width:262px;font-size:8.3px;line-height:10.4px;text-align:justify;color:var(--ink)}
.bio p+p{margin-top:5px}
.bio--one{left:20px}
.bio--two{left:298px}
.bio--three{left:576px}
.skin-photo{left:14px;top:412px;width:116px;height:116px;background:radial-gradient(circle at 50% 45%,#f0cdb4,#d9a98b 60%,#e9d0a6)}
.body-photo{left:136px;top:372px;width:142px;height:142px;background:radial-gradient(circle at 50% 45%,#d4a07c,#b77c58 60%,#e9e4df)}
.location-map{left:292px;top:448px;width:150px;height:94px;border:4px solid #fff;border-radius:6px;
  background:linear-gradient(135deg,#e4ecd9,#d6e2ee 55%,#c9d8e8);box-shadow:0 2px 6px rgba(0,0,0,.3)}
.contact--right{justify-content:flex-end;right:22px}
</style>
</head>
<body>
<main class="canvas">

  <!-- FRONT -->
  <section class="card card--front" aria-label="Postcard front">
    <div class="photo family-photo" role="img" aria-label="Photo of a smiling family of four"></div>
    <svg class="shapes" viewBox="0 0 860 558" aria-hidden="true">
      <defs>
        <linearGradient id="bandF" x1="0" y1="0" x2="0" y2="1">
          <stop offset="0" stop-color="#1a86d6"/><stop offset="1" stop-color="#0455a3"/>
        </linearGradient>
      </defs>
      <path d="M600 0 C665 0 680 72 770 74 L860 74 V58 L770 58 C705 55 690 0 640 0 Z" fill="#1a86d6"/>
      <path d="M640 0 C690 0 705 55 770 58 L860 58 V0 Z" fill="#3b3d42"/>
      <path d="M0 418 C260 372 520 392 860 372 L860 394 C520 414 260 396 0 440 Z" fill="#3b3d42"/>
      <path d="M0 440 C260 396 520 414 860 394 V558 H0 Z" fill="url(#bandF)"/>
    </svg>
    <p class="tab-label">BOOK ONLINE <span>or</span> CALL<br><span>for an appointment</span></p>

    <h1 class="headline">
      <span class="headline__lead">Patient centered</span><br>
      <span class="headline__sub">complete dermatologic care<br>for the whole family</span>
    </h1>

    <div class="specialties">
      <h2 class="specialties__title">Specializing in</h2>
      <ul class="specialties__list">
        <li><svg viewBox="0 0 12 12"><path d="M1 6.5 L4.5 10 L11 2" fill="none" stroke="#fff" stroke-width="1.6"/></svg>Mohs surgery by a Fellowship-Trained Mohs Surgeon</li>
        <li><svg viewBox="0 0 12 12"><path d="M1 6.5 L4.5 10 L11 2" fill="none" stroke="#fff" stroke-width="1.6"/></svg>Comprehensive dermatologic care including medical, cosmetic and surgical dermatology</li>
        <li><svg viewBox="0 0 12 12"><path d="M1 6.5 L4.5 10 L11 2" fill="none" stroke="#fff" stroke-width="1.6"/></svg>Every patient</li>
      </ul>
    </div>

    <div class="brand brand--front">
      <span class="brand__mark"></span>
      <p class="brand__name">Verandell Dermatology<br>and Skin Surgery Associates</p>
    </div>

    <div class="photo photo--circle" role="img" aria-label="Photo of a smiling senior couple" style="left:536px;top:386px;width:130px;height:130px;background:radial-gradient(circle,#8a5f45,#c99a74 55%,#e9dfb0)"></div>
    <div class="photo photo--circle" role="img" aria-label="Photo of a woman with clear skin" style="left:714px;top:394px;width:134px;height:134px;background:radial-gradient(circle,#f2d3bd,#e2b396 60%,#f4efe9)"></div>

    <p class="contact" style="left:30px;top:452px">
      <svg viewBox="0 0 14 14"><path d="M3 1 L5 1 L6 4 L4.5 5.5 C5.5 7.5 6.5 8.5 8.5 9.5 L10 8 L13 9 L13 11 C13 12 12 13 11 13 C5.5 12.5 1.5 8.5 1 3 C1 2 2 1 3 1Z" fill="#fff"/></svg>(555)-014-7280
    </p>
    <p class="contact" style="left:238px;top:452px">
      <svg viewBox="0 0 14 14"><rect x="3" y="1" width="8" height="4" fill="#fff"/><rect x="1" y="5" width="12" height="6" rx="1" fill="#fff"/><rect x="3" y="9" width="8" height="4" fill="#fff" stroke="#0a6fc2"/></svg>(555) 014-5193
    </p>
    <p class="contact" style="left:30px;top:482px">
      <svg viewBox="0 0 14 14"><path d="M7 13 C3 8 2.5 6.5 2.5 5 A4.5 4.5 0 0 1 11.5 5 C11.5 6.5 11 8 7 13Z" fill="#fff"/><circle cx="7" cy="5" r="1.6" fill="#0a6fc2"/></svg>4471 Quillan Avenue, Suite 100 Charlotte, NC 28999
    </p>
    <p class="contact" style="left:30px;top:512px">
      <svg viewBox="0 0 14 14"><circle cx="7" cy="7" r="6" fill="#fff"/></svg>www.VerandellDermatology.example
    </p>
  </section>

  <!-- BACK -->
  <section class="card card--back" aria-label="Postcard back">
    <svg class="shapes" viewBox="0 0 860 558" aria-hidden="true">
      <defs>
        <linearGradient id="bandB" x1="0" y1="0" x2="0" y2="1">
          <stop offset="0" stop-color="#1a86d6"/><stop offset="1" stop-color="#0455a3"/>
        </linearGradient>
      </defs>
      <path d="M0 0 H660 C700 8 705 62 770 66 L860 68 V74 L770 74 C600 70 350 76 0 84 Z" fill="url(#bandB)"/>
      <path d="M640 0 C690 0 705 55 770 58 L860 58 V0 Z" fill="#3b3d42"/>
      <path d="M0 480 C300 470 560 440 860 372 L860 392 C560 460 300 488 0 500 Z" fill="#3b3d42"/>
      <path d="M0 500 C300 488 560 460 860 392 V558 H0 Z" fill="url(#bandB)"/>
    </svg>
    <p class="tab-label">BOOK ONLINE <span>or</span> CALL<br><span>for an appointment</span></p>

    <h1 class="doctor-name">Corinne T. Valdemar, MD, FAAD</h1>
    <p class="doctor-title">Board-Certified Dermatologist and Fellowship-Trained Mohs Surgeon</p>

    <div class="photo photo--circle portrait" role="img" aria-label="Portrait photo of Dr. Valdemar"></div>

    <p class="intro">Dr. Valdemar graduated from the Brackenfield State University Medical School, Sigma Rho Delta, and completed her dermatology residency and Mohs fellowship at Whitcombe University in Atlanta GA. She provides complete dermatologic care for the whole family with a specialization in Mohs surgery.</p>
    <p class="about-pill">About Dr. Valdemar</p>

    <div class="brand brand--back">
      <span class="brand__mark"></span>
      <p class="brand__name">Verandell Dermatology<br>and Skin Surgery Associates</p>
    </div>

    <div class="bio bio--one">
      <p>Dr. Corinne Tolliver Valdemar is a Board-Certified Dermatologist and Fellowship-Trained Mohs Surgeon from Whitcombe University. She graduated Tau Zeta Mu and with highest distinction from the Brackenfield State University. She then received her M.D. and Master’s in Public Health from the Brackenfield State University School of Medicine. Graduating at the top of her class, Dr. Valdemar was inducted into the prestigious Sigma Rho Delta honor society, which is the highest academic honor in medical school.</p>
    </div>
    <div class="bio bio--two">
      <p>Dr. Valdemar completed her internship at Fernhollow hospital in Salt Lake City, Utah. She completed her dermatology residency training at Whitcombe University School of Medicine, serving as the Chief Resident during her final year. During her time as a resident, she received the CUCS resident scholarship award and worked with leading experts in both cutaneous and transplant oncology.</p>
      <p>After her residency she went on to receive highly competitive sub-specialty training and completed her fellowship training in Mohs Micrographic Surgery, Cutaneous Oncology, and Reconstructive Surgery at Whitcombe University Department of Dermatology. This Procedural Dermatology fellowship is certified both by the Federated Board of Margin Surgery (FBMS) and the Physicians’ League Oversight Board for Residency Training (PLOBRT). During her training Dr. Valdemar performed thousands of dermatologic surgeries.</p>
    </div>
    <div class="bio bio--three">
      <p>She has authored numerous scientific articles and textbook chapters, spoken at national meetings and served on numerous committees. Dr. Valdemar is Board Certified in Dermatology and is a Fellow of the National Guild of Skin Medicine and Federated Board of Margin Surgery. She is a member of the National Guild of Skin Medicine, Continental Union of Cutaneous Surgery, Lantern Circle Skin Society, Global Graft Recipient Melanoma Network, Sigma Rho Delta National Honor Society, and Piedmont Skin Physicians Alliance.</p>
      <p>Prior to moving back to North Carolina, she practiced with Riverbend Skin Partners in Cincinnati performing Mohs surgery, skin surgeries, general dermatology, and cosmetics.</p>
    </div>

    <div class="photo photo--circle skin-photo" role="img" aria-label="Photo of a young woman with smooth skin"></div>
    <div class="photo photo--circle body-photo" role="img" aria-label="Photo of a man's torso"></div>
    <div class="photo location-map" role="img" aria-label="Map showing the practice location on Quillan Avenue, Charlotte"></div>

    <p class="contact contact--right" style="top:448px;right:240px">
      (555)-014-7280<svg viewBox="0 0 14 14"><path d="M3 1 L5 1 L6 4 L4.5 5.5 C5.5 7.5 6.5 8.5 8.5 9.5 L10 8 L13 9 L13 11 C13 12 12 13 11 13 C5.5 12.5 1.5 8.5 1 3 C1 2 2 1 3 1Z" fill="#fff"/></svg>
    </p>
    <p class="contact contact--right" style="top:448px">
      (555) 014-5193<svg viewBox="0 0 14 14"><rect x="3" y="1" width="8" height="4" fill="#fff"/><rect x="1" y="5" width="12" height="6" rx="1" fill="#fff"/><rect x="3" y="9" width="8" height="4" fill="#fff" stroke="#0a6fc2"/></svg>
    </p>
    <p class="contact contact--right" style="top:480px">
      4471 Quillan Avenue, Suite 100 Charlotte, NC 28999<svg viewBox="0 0 14 14"><path d="M7 13 C3 8 2.5 6.5 2.5 5 A4.5 4.5 0 0 1 11.5 5 C11.5 6.5 11 8 7 13Z" fill="#fff"/><circle cx="7" cy="5" r="1.6" fill="#0a6fc2"/></svg>
    </p>
    <p class="contact contact--right" style="top:512px">
      www.VerandellDermatology.example<svg viewBox="0 0 14 14"><circle cx="7" cy="7" r="6" fill="#fff"/></svg>
    </p>
  </section>

</main>
</body>
</html>
```